Brightmoor Capital
"The Business and Corporate Finance Specialists, Mortgages and Remortgages"
Professional
Dorian Kellaway
Director
14 Quillfield Parade
Harrow
London
HA7 2QX
Dorian@brightmoorcapital.example
www.brightmoorcapital.example
Letterhead and compliment slips require the following regulatory text:
"Registered in England and Wales number: 08213947
Brightmoor Capital Ltd is authorised and regulated by the Monetary Oversight Council for regulated mortgage contracts and non-investment insurance activities."
Be creative - open to suggestions

```html
<!DOCTYPE html>
<html lang="en">
<head>
<meta charset="utf-8">
<title>Brightmoor Capital – Business Card</title>
<link rel="stylesheet" href="https://fonts.googleapis.com/css2?family=Didact+Gothic&family=Open+Sans:wght@400;700&display=swap">
<style>
  :root {
    --stage: #e9e6e1;
    --card-top: #1c1c1c;
    --card-bottom: #050505;
    --band-orange: #f07a12;
    --band-yellow: #f9b21c;
    --accent-green: #8cc63f;
    --text-light: #f2f2f2;
    --name-orange: #f28c1a;
    --role-orange: #c9701a;
  }
  * { margin: 0; padding: 0; box-sizing: border-box; }
  html, body { width: 1200px; height: 780px; overflow: hidden; background: var(--stage); }
  .stage { position: relative; width: 1200px; height: 780px; }
  .card {
    position: absolute; left: 100px; top: 90px; width: 1000px; height: 600px;
    border-radius: 34px; overflow: hidden;
    background: linear-gradient(160deg, var(--card-top), var(--card-bottom) 70%);
    box-shadow: 0 14px 34px rgba(0,0,0,.28);
    font-family: "Open Sans", sans-serif; color: var(--text-light);
  }
  .band {
    position: absolute; left: 48px; top: 0; width: 118px; height: 100%;
    background: linear-gradient(90deg, var(--band-orange), var(--band-yellow) 55%, var(--band-orange));
    border-left: 4px solid var(--accent-green);
    border-right: 2px solid var(--accent-green);
  }
  .band::before {
    content: ""; position: absolute; left: 8px; top: 0; width: 2px; height: 100%;
    background: var(--accent-green);
  }
  .company {
    position: absolute; left: 196px; top: 118px;
    font-family: "Didact Gothic", sans-serif; font-size: 58px; color: var(--text-light);
    letter-spacing: 0.5px;
  }
  .tagline {
    position: absolute; left: 200px; top: 196px;
    font-family: "Didact Gothic", sans-serif; font-size: 17px; line-height: 21px;
    color: var(--text-light); letter-spacing: 0.3px;
  }
  .address { position: absolute; left: 236px; top: 282px; font-size: 21px; line-height: 30px; }
  .contacts { position: absolute; left: 204px; top: 350px; list-style: none; }
  .contacts li { display: flex; align-items: center; height: 36px; font-size: 21px; }
  .contacts svg { width: 22px; height: 22px; margin-right: 10px; flex: none; }
  .person { position: absolute; left: 700px; top: 312px; text-align: center; width: 240px; }
  .person-name { font-size: 27px; font-weight: 700; color: var(--name-orange); }
  .person-role { font-size: 17px; color: var(--role-orange); margin-top: 2px; }
</style>
</head>
<body>
<main class="stage">
  <section class="card" aria-label="Brightmoor Capital business card">
    <div class="band"></div>

    <h1 class="company">Brightmoor Capital</h1>
    <p class="tagline">Business and Corporate Finance Specialists<br>Mortgages and Remortgages</p>

    <address class="address" style="font-style:normal">
      14 Quillfield Parade<br>Harrow, London, HA7 2QX
    </address>

    <ul class="contacts">
      <li>
        <svg viewBox="0 0 24 24" aria-hidden="true"><path fill="#f07a12" d="M6.6 10.8a15 15 0 0 0 6.6 6.6l2.2-2.2c.3-.3.7-.4 1-.2 1.1.4 2.3.6 3.6.6.6 0 1 .4 1 1V20c0 .6-.4 1-1 1A17 17 0 0 1 3 4c0-.6.4-1 1-1h3.5c.6 0 1 .4 1 1 0 1.3.2 2.5.6 3.6.1.3 0 .7-.2 1z"/></svg>
        +44 (0) 208 555 0142
      </li>
      <li>
        <svg viewBox="0 0 24 24" aria-hidden="true"><rect x="7" y="2" width="10" height="20" rx="2" fill="#f07a12"/><rect x="9" y="5" width="6" height="11" fill="#111"/></svg>
        +44 (0) 7700 900 361
      </li>
      <li>
        <svg viewBox="0 0 24 24" aria-hidden="true"><rect x="3" y="9" width="18" height="11" rx="2" fill="#f07a12"/><rect x="7" y="3" width="10" height="7" fill="#f07a12"/><rect x="7" y="13" width="10" height="2" fill="#111"/></svg>
        +44 (0) 208 555 0187
      </li>
      <li>
        <svg viewBox="0 0 24 24" aria-hidden="true"><circle cx="12" cy="12" r="11" fill="#f07a12"/><text x="12" y="16.5" font-size="13" font-family="Open Sans, sans-serif" font-weight="700" text-anchor="middle" fill="#111">@</text></svg>
        Dorian@brightmoorcapital.example
      </li>
      <li>
        <svg viewBox="0 0 24 24" aria-hidden="true"><circle cx="12" cy="12" r="11" fill="#f07a12"/><g fill="none" stroke="#111" stroke-width="1.4"><circle cx="12" cy="12" r="7"/><ellipse cx="12" cy="12" rx="3" ry="7"/><path d="M5 12h14"/></g></svg>
        www.brightmoorcapital.example
      </li>
    </ul>

    <div class="person">
      <p class="person-name">Dorian Kellaway</p>
      <p class="person-role">Director</p>
    </div>
  </section>
</main>
</body>
</html>
```